Delivery Performance Dashboard for Web Portal

We need you to design a dashboard for our web portal. We deliver sand and stone to construction jobsites. The attached screenshot is from our current web portal dashboard . It shows how much material has been delivered from an order.

Dump trucks will deliver multiple loads during the day and the dispatcher uses the dashboard to monitor if they need to add more trucks or less trucks to fulfill the order. An example would be, I need to ship 1,000 tons of sand to a jobsite and I plan to use 10 trucks during the day and that it will take 10 hours of hauling to complete the job. After 5 hours of hauling (50% the day is over), I should have delivered 500 tons of sand (50% of the order). But maybe there is a lot of traffic, and I only have delivered 300 tons. The dashboard will show that I am behind schedule and I might need to add 2 more trucks to the job.

Industry/Entity Type

Construction

Font styles to use
Sans Serif

Requirements
Must have
• We need a progress bar showing how much material has been delivered, how much material was requested to be delivered total and how much material should have been delivered at the current time. The goal is to show the user if the deliveries are ahead or behind the expected pace and why.
Nice to have
• The icons for plant, driving and jobsite show if the actual times have exceeded or beaten the planned times. Maybe you have other ideas to show the user if the trucks are sitting longer on the jobsite, at the plant to get loaded or driving to and from the jobsite.

```html
<!DOCTYPE html>
<html lang="en">
<head>
<meta charset="utf-8">
<title>Dump Trucks – Delivery Dashboard</title>
<link href="https://fonts.googleapis.com/css2?family=Montserrat:wght@600;800&family=Open+Sans:wght@400;600;700&display=swap" rel="stylesheet">
<style>
:root{
  --page:#e9ebee;
  --navy:#1d2a5c;
  --navy-dark:#17224d;
  --panel:#ffffff;
  --table-head:#4a4a4a;
  --line:#e3e5e8;
  --text:#555b66;
  --muted:#9aa0a8;
  --green:#3fae49;
  --red:#d9534f;
  --cyan:#2ab6e6;
  --icon:#6b7280;
}
*{box-sizing:border-box;margin:0;padding:0}
html,body{width:828px;height:1200px;overflow:hidden}
body{background:var(--page);font-family:"Open Sans",Arial,sans-serif;color:var(--text);font-size:6px}
.screen{position:absolute;left:14px;width:800px;height:578px;background:#f3f4f6;box-shadow:0 1px 4px rgba(0,0,0,.15);overflow:hidden}
.screen.first{top:8px}
.screen.second{top:610px}
.topbar{position:absolute;left:0;top:0;right:0;height:30px;background:var(--navy);display:flex;align-items:center;padding:0 10px}
.menu-btn{width:12px;display:flex;flex-direction:column;gap:2px}
.menu-btn span{display:block;height:1.5px;background:#fff}
.brand{margin-left:58px;font-family:"Montserrat",Arial,sans-serif;font-weight:800;color:#fff;font-size:13px;letter-spacing:.5px}
.search{margin-left:auto;width:92px;height:12px;border-radius:6px;background:#fff;display:flex;align-items:center;justify-content:space-between;padding:0 1px 0 6px;color:var(--muted);font-size:5.5px}
.search i{width:10px;height:10px;border-radius:50%;background:var(--green);display:block}
.user{margin-left:18px;text-align:right;color:#fff;line-height:1.2}
.user small{display:block;font-size:5px;color:#c5cbe0}
.user b{font-size:7.5px;font-weight:700}
.avatar{margin-left:6px;width:20px;height:20px;border-radius:50%;background:linear-gradient(#8a7a6a,#3f3a36);border:1.5px solid #fff}
.sidebar{position:absolute;left:0;top:30px;bottom:0;width:72px;background:var(--navy-dark);padding-top:6px}
.sidebar li{list-style:none;display:flex;align-items:center;gap:5px;color:#d9deef;font-size:5.5px;padding:3px 8px}
.sidebar li i{width:5px;height:5px;border:1px solid #aeb6d6;border-radius:1px;display:block}
.content{position:absolute;left:72px;top:30px;right:0;bottom:0;padding:14px 22px 0 22px}
.card{background:var(--panel);box-shadow:0 1px 2px rgba(0,0,0,.08);margin-bottom:10px}
table{width:100%;border-collapse:collapse}
th{background:var(--table-head);color:#fff;font-size:5.5px;font-weight:700;text-align:left;padding:6px 8px;letter-spacing:.3px}
td{font-size:5px;padding:6px 8px;border-bottom:1px solid var(--line);color:var(--text);height:20px;vertical-align:middle}
.pager{display:flex;justify-content:flex-end;gap:3px;padding:8px 10px}
.pager span{width:9px;height:9px;border:1px solid var(--line);display:flex;align-items:center;justify-content:center;font-size:5px;color:var(--muted)}
.pager span.on{background:var(--green);border-color:var(--green);color:#fff}
.orders-card{height:122px;position:relative}
.orders-card .pager{position:absolute;right:0;bottom:0}
.loads-card{height:128px;position:relative}
.loads-card .pager{position:absolute;right:0;bottom:0}
.loads td{height:22px}
.bar{width:74px;height:3px;background:#dfe3e7;position:relative;margin-bottom:3px}
.bar b{position:absolute;left:0;top:0;bottom:0;background:var(--cyan)}
.bar.mark::after{content:"";position:absolute;top:-2px;width:1px;height:7px;background:var(--navy);left:var(--pace)}
.tons{font-size:4.5px;color:var(--muted)}
.stages{display:flex;align-items:center;gap:4px}
.stages svg{display:block}
.ok{color:var(--green)}
.late{color:var(--red)}
.th-icons{display:flex;align-items:center;gap:4px}
.footer{position:absolute;left:72px;right:0;bottom:10px;text-align:center;font-size:4.5px;color:var(--muted)}
.pageno{position:absolute;right:8px;bottom:8px;font-size:4.5px;color:var(--muted)}
.popup{position:absolute;left:312px;top:348px;width:92px;background:#fff;box-shadow:0 2px 8px rgba(0,0,0,.25);border-radius:2px;padding:6px 7px}
.popup::before{content:"";position:absolute;top:-4px;left:40px;border:4px solid transparent;border-top:0;border-bottom-color:#fff}
.popup h4{font-size:7px;font-weight:600;color:var(--text);padding-bottom:4px;border-bottom:1px solid var(--line);margin-bottom:3px}
.popup .row{display:flex;align-items:center;gap:6px;padding:4px 0;border-bottom:1px solid var(--line);font-size:4.5px}
.popup .row:last-child{border-bottom:0}
.popup .row .lbl{flex:1;line-height:1.3}
.popup .row .act{color:var(--muted)}
</style>
</head>
<body>

<!-- Screen: overview -->
<section class="screen first">
  <header class="topbar">
    <div class="menu-btn"><span></span><span></span><span></span></div>
    <div class="brand">DUMP TRUCKS</div>
    <div class="search">Search <i></i></div>
    <div class="user"><small>Welcome</small><b>Alex Reyes</b></div>
    <div class="avatar" role="img" aria-label="User profile photo"></div>
  </header>
  <ul class="sidebar">
    <li><i></i>Home</li><li><i></i>Timesheets ▾</li><li><i></i>Receipts ▾</li><li><i></i>Reports</li><li><i></i>Messages</li><li><i></i>Contact</li>
  </ul>
  <main class="content">
    <div class="card orders-card">
      <table>
        <tr><th>ORDER</th><th>ORIGIN</th><th>DESTINATION</th><th>CUSTOMER</th><th>STATUS</th></tr>
        <tr><td>7T745</td><td>North sand pit plant</td><td>820 - 150 Oak Valley Drive</td><td>Construction - North Division</td><td>Scheduled</td></tr>
        <tr><td>3A456</td><td>East stone quarry</td><td>820 - 150 Oak Valley Drive</td><td>Construction - North Division</td><td>Scheduled</td></tr>
        <tr><td>7T745</td><td>North sand pit plant</td><td>820 - 150 Oak Valley Drive</td><td>Construction - North Division</td><td>Scheduled</td></tr>
      </table>
      <div class="pager"><span>‹</span><span class="on">1</span><span>›</span></div>
    </div>

    <div class="card loads-card">
      <table class="loads">
        <tr><th>TONS</th><th>WAIT TIMES</th><th><span class="th-icons">◷ REMAINING</span></th><th></th></tr>
        <tr>
          <td><div class="bar mark" style="--pace:60%"><b style="width:78%"></b></div><span class="tons">780 / 1000</span></td>
          <td><div class="stages">
            <svg width="12" height="8" viewBox="0 0 12 8"><rect x="0" y="3" width="5" height="5" fill="var(--icon)"/><rect x="5" y="0" width="7" height="8" fill="var(--icon)"/></svg>
            <svg width="12" height="8" viewBox="0 0 12 8"><rect x="0" y="1" width="8" height="5" fill="var(--red)"/><rect x="8" y="3" width="4" height="3" fill="var(--red)"/><circle cx="2.5" cy="7" r="1" fill="var(--red)"/><circle cx="9" cy="7" r="1" fill="var(--red)"/></svg>
            <svg width="12" height="8" viewBox="0 0 12 8"><path d="M6 0 L12 8 H0 Z" fill="var(--icon)"/></svg>
          </div></td>
          <td class="ok">+ 15 min</td><td class="late">2h</td>
        </tr>
        <tr>
          <td><div class="bar mark" style="--pace:70%"><b style="width:55%"></b></div><span class="tons">550 / 1000</span></td>
          <td><div class="stages">
            <svg width="12" height="8" viewBox="0 0 12 8"><rect x="0" y="3" width="5" height="5" fill="var(--icon)"/><rect x="5" y="0" width="7" height="8" fill="var(--icon)"/></svg>
            <svg width="12" height="8" viewBox="0 0 12 8"><rect x="0" y="1" width="8" height="5" fill="var(--red)"/><rect x="8" y="3" width="4" height="3" fill="var(--red)"/><circle cx="2.5" cy="7" r="1" fill="var(--red)"/><circle cx="9" cy="7" r="1" fill="var(--red)"/></svg>
            <svg width="12" height="8" viewBox="0 0 12 8"><path d="M6 0 L12 8 H0 Z" fill="var(--icon)"/></svg>
          </div></td>
          <td class="ok">+ 30 min</td><td class="late">3h</td>
        </tr>
        <tr>
          <td><div class="bar mark" style="--pace:40%"><b style="width:30%"></b></div><span class="tons">300 / 1000</span></td>
          <td><div class="stages">
            <svg width="12" height="8" viewBox="0 0 12 8"><rect x="0" y="3" width="5" height="5" fill="var(--icon)"/><rect x="5" y="0" width="7" height="8" fill="var(--icon)"/></svg>
            <svg width="12" height="8" viewBox="0 0 12 8"><rect x="0" y="1" width="8" height="5" fill="var(--red)"/><rect x="8" y="3" width="4" height="3" fill="var(--red)"/><circle cx="2.5" cy="7" r="1" fill="var(--red)"/><circle cx="9" cy="7" r="1" fill="var(--red)"/></svg>
            <svg width="12" height="8" viewBox="0 0 12 8"><path d="M6 0 L12 8 H0 Z" fill="var(--icon)"/></svg>
          </div></td>
          <td class="ok">+ 10 min</td><td class="late">5h</td>
        </tr>
      </table>
      <div class="pager"><span>‹</span><span class="on">1</span><span>›</span></div>
    </div>
  </main>
  <div class="footer">© 2024 Granite Haul Co. All Rights Reserved | Privacy | Terms and Use | Find your agreement | Contact reference</div>
  <div class="pageno">01</div>
</section>

<!-- Screen: order detail popup -->
<section class="screen second">
  <header class="topbar">
    <div class="menu-btn"><span></span><span></span><span></span></div>
    <div class="brand">DUMP TRUCKS</div>
    <div class="search">Search <i></i></div>
    <div class="user"><small>Welcome</small><b>Alex Reyes</b></div>
    <div class="avatar" role="img" aria-label="User profile photo"></div>
  </header>
  <ul class="sidebar">
    <li><i></i>Home</li><li><i></i>Timesheets ▾</li><li><i></i>Receipts ▾</li><li><i></i>Reports</li><li><i></i>Messages</li><li><i></i>Contact</li>
  </ul>
  <main class="content">
    <div class="card orders-card">
      <table>
        <tr><th>ORDER</th><th>ORIGIN</th><th>DESTINATION</th><th>CUSTOMER</th><th>STATUS</th></tr>
        <tr><td>7T745</td><td>North sand pit plant</td><td>820 - 150 Oak Valley Drive</td><td>Construction - North Division</td><td>Scheduled</td></tr>
        <tr><td>3A456</td><td>East stone quarry</td><td>820 - 150 Oak Valley Drive</td><td>Construction - North Division</td><td>Scheduled</td></tr>
        <tr><td>7T745</td><td>North sand pit plant</td><td>820 - 150 Oak Valley Drive</td><td>Construction - North Division</td><td>Scheduled</td></tr>
      </table>
      <div class="pager"><span>‹</span><span class="on">1</span><span>›</span></div>
    </div>

    <div class="card loads-card">
      <table class="loads">
        <tr><th>TONS</th><th>WAIT TIMES</th><th><span class="th-icons">◷ REMAINING</span></th><th></th></tr>
        <tr>
          <td><div class="bar mark" style="--pace:60%"><b style="width:78%"></b></div><span class="tons">780 / 1000</span></td>
          <td><div class="stages">
            <svg width="12" height="8" viewBox="0 0 12 8"><rect x="0" y="3" width="5" height="5" fill="var(--icon)"/><rect x="5" y="0" width="7" height="8" fill="var(--icon)"/></svg>
            <svg width="12" height="8" viewBox="0 0 12 8"><rect x="0" y="1" width="8" height="5" fill="var(--red)"/><rect x="8" y="3" width="4" height="3" fill="var(--red)"/><circle cx="2.5" cy="7" r="1" fill="var(--red)"/><circle cx="9" cy="7" r="1" fill="var(--red)"/></svg>
            <svg width="12" height="8" viewBox="0 0 12 8"><path d="M6 0 L12 8 H0 Z" fill="var(--icon)"/></svg>
          </div></td>
          <td class="ok">+ 15 min</td><td class="late">2h</td>
        </tr>
        <tr>
          <td><div class="bar mark" style="--pace:70%"><b style="width:55%"></b></div><span class="tons">550 / 1000</span></td>
          <td></td><td></td><td></td>
        </tr>
        <tr>
          <td><div class="bar mark" style="--pace:40%"><b style="width:30%"></b></div><span class="tons">300 / 1000</span></td>
          <td></td><td></td><td></td>
        </tr>
      </table>
    </div>
  </main>

  <div class="popup">
    <h4>Order : 7T745</h4>
    <div class="row">
      <svg width="10" height="8" viewBox="0 0 10 8"><path d="M0 2 H8 M6 0 L8 2 L6 4 M10 6 H2 M4 4 L2 6 L4 8" stroke="var(--icon)" fill="none"/></svg>
      <span class="lbl">Avg Load Time: 2 hr (Plan)</span>
    </div>
    <div class="row">
      <svg width="10" height="8" viewBox="0 0 10 8"><rect x="0" y="3" width="4" height="5" fill="var(--icon)"/><rect x="4" y="0" width="6" height="8" fill="var(--icon)"/></svg>
      <span class="lbl">Plant time<br>Planned: 30</span><span class="act">Actual: 35</span>
    </div>
    <div class="row">
      <svg width="10" height="8" viewBox="0 0 10 8"><rect x="0" y="1" width="7" height="5" fill="var(--red)"/><rect x="7" y="3" width="3" height="3" fill="var(--red)"/></svg>
      <span class="lbl">Drive time<br>Planned: 40</span><span class="act">Actual: 55</span>
    </div>
    <div class="row">
      <svg width="10" height="8" viewBox="0 0 10 8"><path d="M5 0 L10 8 H0 Z" fill="var(--icon)"/></svg>
      <span class="lbl">Jobsite time<br>Planned: 20</span><span class="act">Actual: 25</span>
    </div>
    <div class="row">
      <svg width="10" height="8" viewBox="0 0 10 8"><path d="M5 0 C8 0 8 4 5 8 C2 4 2 0 5 0 Z" fill="var(--cyan)"/></svg>
      <span class="lbl">Trucks on job</span><span class="act">Actual: 10</span>
    </div>
  </div>

  <div class="footer">© 2024 Granite Haul Co. All Rights Reserved | Privacy | Terms and Use | Find your agreement | Contact reference</div>
  <div class="pageno">02</div>
</section>

</body>
</html>
```